"Rise. Shift. Thrive." Empowerment Book Cover

Hello, I need a hot, trendy, and contemporary book cover designed for my first book called "Rise. Shift. Thrive. -- 360 Bold Momentum Notes to Guide Anyone to Rise, Shift, and Thrive in Their Career & Daily Dreams."
This is my first book and I am really wanting to launch my brand with it... it would be awesome to match the inside/outside branding of the book. So we can either create the book cover to match the book guts, or update the book guts to match the cover.
Lastly, I just got a professional photoshoot done last week so we can use one of those images, or we can go with a different idea/style for the cover. The body of the book is attached. All questions welcomed, happy designing!
Target Market(s)
Gen Z, Millennials and Gen X.
Industry/Entity Type
Personal Development.
Requirements
Must have
- It must stand out and be different from other typical book covers.
Nice to have
- Success, Inspiration, Motivation, Mindset, Growth.
Should not have
- Clipart, stock art, stock look and feel.

```html
<!DOCTYPE html>
<html lang="en">
<head>
<meta charset="utf-8">
<title>Rise. Shift. Thrive. — Book Cover</title>
<link href="https://fonts.googleapis.com/css2?family=Poppins:wght@400;500;700;800&family=Playfair+Display:wght@500&display=swap" rel="stylesheet">
<style>
  :root {
    --stage: #053a5a;
    --sand: #c9a77a;
    --surf: #8fa9a0;
    --shallow: #2f8589;
    --deep: #1a5a86;
    --deepest: #134c82;
    --panel: #6fd9c9;
    --ink: #0f3558;
    --white: #ffffff;
    --word-one: #7ccfee;
    --word-two: #5fd6c0;
    --word-three: #c9f0e8;
  }
  * { margin: 0; padding: 0; box-sizing: border-box; }
  html, body {
    width: 1200px; height: 1200px; overflow: hidden;
    background: var(--stage);
  }
  .canvas { position: relative; width: 1200px; height: 1200px; }
  .cover {
    position: absolute; left: 291px; top: 136px;
    width: 618px; height: 927px; overflow: hidden;
  }
  .cover-photo {
    position: absolute; inset: 0;
    background: linear-gradient(180deg,
      var(--sand) 0%, #c8aa80 16%, var(--surf) 30%,
      #9fb8b3 45%, var(--shallow) 62%, var(--deep) 82%, var(--deepest) 100%);
  }
  .author {
    position: absolute; left: 326px; top: 66px;
    font-family: "Poppins", sans-serif; font-weight: 700;
    font-size: 37px; line-height: 41px; letter-spacing: -0.5px;
    color: var(--white);
  }
  .subtitle-panel {
    position: absolute; left: 312px; top: 209px;
    width: 306px; height: 205px;
    background: var(--panel); color: var(--ink);
    padding: 22px 0 0 22px;
    font-family: "Poppins", sans-serif; font-size: 14px; line-height: 20px;
  }
  .subtitle-number {
    font-family: "Playfair Display", serif; font-weight: 500;
    font-size: 36px; line-height: 36px; margin-bottom: 4px;
  }
  .subtitle-lead { font-weight: 700; }
  .subtitle-rest { font-weight: 400; }
  .title {
    position: absolute; left: 0; top: 0; width: 1200px; height: 1200px;
    pointer-events: none;
  }
  .title text {
    font-family: "Poppins", sans-serif; font-weight: 800;
    font-size: 100px; letter-spacing: -3px;
  }
  .word-one { fill: var(--word-one); }
  .word-two { fill: var(--word-two); }
  .word-three { fill: var(--word-three); }
</style>
</head>
<body>
<div class="canvas">
  <div class="cover">
    <div class="cover-photo" role="img" aria-label="Aerial photograph of a sandy beach with white surf breaking into deep blue-green sea"></div>
    <div class="author">Idris<br>Halden</div>
    <div class="subtitle-panel">
      <div class="subtitle-number">360</div>
      <div class="subtitle-lead">Bold<br>Momentum Notes<br>to Guide Anyone</div>
      <div class="subtitle-rest">Rise, Shift and Thrive in<br>Their Career &amp; Daily<br>Dreams</div>
    </div>
  </div>
  <svg class="title" viewBox="0 0 1200 1200" aria-label="Rise. Shift. Thrive.">
    <text class="word-one" transform="translate(532 1015) rotate(-90)">Rise.</text>
    <text class="word-two" transform="translate(707 1015) rotate(-90)">Shift.</text>
    <text class="word-three" transform="translate(857 1015) rotate(-90)">Thrive.</text>
  </svg>
</div>
</body>
</html>
```